Cell phone repair

you can please design me business card

size 3.5" x 2"

colors blue and red

fixit dash logo (you get from my website fixitdashhq.com )

"We Come To You!

It is very simple! You tell us what phone you have, And we come to fix it."

phone number: 412.586.3094

website: www.fixitdashhq.com

email: info@fixitdashhq.com

```html
<!DOCTYPE html>
<html lang="en">
<head>
<meta charset="utf-8">
<title>fixit dash — Business Card</title>
<link href="https://fonts.googleapis.com/css2?family=Work+Sans:wght@400;500;600&display=swap" rel="stylesheet">
<style>
  :root {
    --brand-blue: #22a7e0;
    --brand-red: #e91e26;
    --paper: #ffffff;
    --ink: #3a3a3a;
    --muted: #555555;
    --stage: #e9ecef;
  }
  * { box-sizing: border-box; margin: 0; padding: 0; }
  html, body {
    width: 1200px; height: 738px; overflow: hidden;
    background: var(--stage);
    font-family: "Work Sans", Arial, sans-serif;
  }
  .sheet {
    width: 1200px; height: 738px;
    display: flex; align-items: center; justify-content: center; gap: 40px;
  }
  .card {
    position: relative; width: 520px; height: 297px; overflow: hidden;
    box-shadow: 0 6px 18px rgba(0,0,0,.18);
  }

  /* Front */
  .card--front {
    background: var(--brand-blue);
    display: flex; align-items: center; justify-content: center;
  }
  .brand { display: flex; align-items: center; gap: 12px; }
  .brand__name { font-weight: 600; letter-spacing: .2px; }
  .brand__dot { border-radius: 50%; flex: none; }
  .card--front .brand__name { color: var(--paper); font-size: 38px; }
  .card--front .brand__dot { width: 34px; height: 34px; border: 5px solid var(--paper); }

  /* Back */
  .card--back { background: var(--paper); }
  .card--back .brand { position: absolute; left: 30px; top: 34px; gap: 10px; }
  .card--back .brand__name { color: var(--brand-blue); font-size: 24px; }
  .card--back .brand__dot { width: 30px; height: 30px; background: var(--brand-red); }

  .holder { position: absolute; right: 28px; top: 48px; text-align: right; }
  .holder__name { color: var(--brand-blue); font-size: 22px; font-weight: 500; letter-spacing: .3px; }
  .holder__role { color: var(--muted); font-size: 11px; margin-top: 4px; }
  .rule { position: absolute; left: 30px; right: 90px; top: 106px; height: 2px; background: var(--brand-red); }

  .contact { position: absolute; left: 30px; top: 128px; list-style: none; }
  .contact__item {
    display: flex; align-items: center; gap: 8px;
    color: var(--ink); font-size: 13px; line-height: 20px;
  }
  .contact__icon { width: 10px; height: 10px; flex: none; }
  .contact__accent { color: var(--brand-red); }

  .footer-stripe {
    position: absolute; left: 0; right: 0; top: 222px; height: 5px;
    background: var(--brand-red);
  }
  .footer-band {
    position: absolute; left: 0; right: 0; top: 231px; bottom: 0;
    background: var(--brand-blue);
  }
  .address {
    position: absolute; right: 28px; top: 246px; text-align: right;
    color: var(--paper); font-size: 12px; line-height: 17px; font-style: normal;
  }
</style>
</head>
<body>
<main class="sheet">
  <section class="card card--front" aria-label="Card front">
    <div class="brand">
      <span class="brand__name">fixit dash</span>
      <span class="brand__dot"></span>
    </div>
  </section>

  <section class="card card--back" aria-label="Card back">
    <div class="brand">
      <span class="brand__name">fixit dash</span>
      <span class="brand__dot"></span>
    </div>

    <div class="holder">
      <p class="holder__name">DANA WHITLOCK</p>
      <p class="holder__role">Director</p>
    </div>
    <div class="rule"></div>

    <ul class="contact">
      <li class="contact__item">
        <svg class="contact__icon" viewBox="0 0 10 10"><path fill="var(--brand-blue)" d="M2 0.5 L3.6 2.6 L2.7 3.6 Q3.8 6 6.4 7.3 L7.4 6.4 L9.5 8 L8.3 9.5 Q1.5 8.5 0.5 1.7 Z"/></svg>
        <span>412.586.3094</span>
      </li>
      <li class="contact__item">
        <svg class="contact__icon" viewBox="0 0 10 10"><rect x="0.7" y="2" width="8.6" height="6" fill="none" stroke="var(--brand-blue)" stroke-width="1.2"/><path d="M0.7 2 L5 5.4 L9.3 2" fill="none" stroke="var(--brand-blue)" stroke-width="1.2"/></svg>
        <span>info@fixitdashhq.com</span>
      </li>
      <li class="contact__item">
        <svg class="contact__icon" viewBox="0 0 10 10"><circle cx="5" cy="5" r="4.2" fill="none" stroke="var(--brand-blue)" stroke-width="1.1"/><path d="M0.8 5 H9.2 M5 0.8 Q2.4 5 5 9.2 M5 0.8 Q7.6 5 5 9.2" fill="none" stroke="var(--brand-blue)" stroke-width="0.9"/></svg>
        <span>www.<span class="contact__accent">fixitdashhq</span>.com</span>
      </li>
    </ul>

    <div class="footer-stripe"></div>
    <div class="footer-band"></div>
    <address class="address">1847 Maple Ridge Road<br>Dayton, OH 45402</address>
  </section>
</main>
</body>
</html>
```